Four In The Door Direct Postcard Marketing Campaign.

I would like a series of four postcards for a direct mail campaign. They will be sent out once a week. The campaign is aimed at human resources professionals. We are a 25 year old staffing company breaking into a new market. I would like a funny or creative campaign built around the theme "All Things Employees" Our company strengths lie in our responsive customer service, our integrity, our expertise and our professionalism. Our website is www.alliedwithmavens.com if you would like more information about our company. Our company colors are red, white and black. I like statistics, quotes, etc. I would like to get the campaign out in early December so Iam working on a tight schedule.

Target Market(s)

Human Resources Managers
Plant Managers
Business Owners

Industry/Entity Type

Marketing

Requirements
Must have
• Tag Line All Things Employees or Allied with Mavens

```html
<!DOCTYPE html>
<html lang="en">
<head>
<meta charset="utf-8">
<title>All Things Employees – Postcard</title>
<link href="https://fonts.googleapis.com/css2?family=Bungee&family=Montserrat:wght@400;600;800&display=swap" rel="stylesheet">
<style>
  :root {
    --ink: #0b0b0b;
    --paper: #f4f4f2;
    --red: #c8102e;
    --grey-light: #d9d9d9;
    --grey-mid: #8c8c8c;
    --grey-dark: #3b3b3b;
    --stage: #e7e4df;
    --display: "Bungee", "Arial Black", sans-serif;
    --body: "Montserrat", Arial, sans-serif;
  }
  * { box-sizing: border-box; margin: 0; padding: 0; }
  html, body { width: 1200px; height: 723px; overflow: hidden; }
  body {
    background: var(--stage);
    font-family: var(--body);
    display: flex;
    align-items: center;
    justify-content: center;
    gap: 48px;
  }

  /* ---------- Back side (mailing side) ---------- */
  .card-back {
    position: relative;
    width: 600px;
    height: 400px;
    background: var(--paper);
    border: 10px solid var(--ink);
    overflow: hidden;
  }
  .card-back .stamp-box {
    position: absolute;
    top: 22px; right: 24px;
    width: 64px; height: 70px;
    border: 2px dashed var(--ink);
    background: #fff;
  }
  .card-back .address-lines {
    position: absolute;
    top: 110px; right: 24px;
    width: 220px;
    display: flex; flex-direction: column; gap: 26px;
  }
  .card-back .address-lines span {
    display: block; height: 2px; background: var(--grey-mid);
  }
  .card-back .brand {
    position: absolute;
    top: 34px; left: 30px;
    display: flex; align-items: center; gap: 10px;
  }
  .brand-dot {
    width: 16px; height: 16px; border-radius: 50%; background: var(--red);
  }
  .brand-name {
    font-weight: 800; font-size: 24px; color: var(--ink); line-height: 1;
  }
  .card-back .tagline {
    position: absolute;
    top: 72px; left: 30px;
    font-size: 12px; font-weight: 600; color: var(--ink);
  }
  .card-back .quote {
    position: absolute;
    left: 30px; bottom: 28px;
    font-family: var(--display);
    font-size: 30px;
    line-height: 1.02;
    color: var(--ink);
    text-transform: uppercase;
  }
  .quote .line { display: block; }
  .quote .indent-1 { padding-left: 24px; }
  .quote .indent-2 { padding-left: 48px; }

  /* ---------- Front side ---------- */
  .card-front {
    position: relative;
    width: 420px;
    height: 600px;
    background: var(--ink);
    overflow: hidden;
  }
  .card-front .suit-art {
    position: absolute;
    top: 0; right: 0;
    width: 270px; height: 470px;
    background: linear-gradient(160deg, var(--grey-light) 0%, var(--grey-mid) 45%, var(--red) 46%, var(--red) 58%, var(--grey-dark) 59%, #5a5a5a 100%);
    clip-path: polygon(0 0, 100% 0, 100% 100%, 40% 100%, 0 70%);
  }
  .card-front .accent {
    position: absolute;
    top: 220px; left: 0;
    width: 0; height: 0;
    border-top: 70px solid transparent;
    border-left: 150px solid var(--red);
  }
  .card-front .title-band {
    position: absolute;
    top: 270px; left: 0;
    width: 100%; height: 190px;
    background: var(--grey-dark);
  }
  .card-front .title {
    position: absolute;
    top: 285px; left: 34px;
    font-family: var(--display);
    font-size: 46px;
    line-height: 1.08;
    color: #fff;
    text-transform: uppercase;
  }
  .card-front .brand {
    position: absolute;
    right: 26px; bottom: 26px;
    display: flex; align-items: center; gap: 8px;
  }
  .card-front .brand-name { color: #fff; font-size: 18px; }
  .card-front .brand-dot { width: 12px; height: 12px; background: #fff; }
</style>
</head>
<body>

  <section class="card-back" aria-label="Postcard back">
    <div class="stamp-box"></div>
    <div class="address-lines">
      <span></span><span></span><span></span><span></span>
    </div>
    <div class="brand">
      <span class="brand-dot"></span>
      <span class="brand-name">Staffwell Partners</span>
    </div>
    <p class="tagline">All Things Employees or Allied with Mavens</p>
    <p class="quote">
      <span class="line">The greatest</span>
      <span class="line indent-1">pleasure</span>
      <span class="line indent-2">in life</span>
      <span class="line">is doing</span>
      <span class="line">what people say</span>
      <span class="line indent-1">you cannot do</span>
    </p>
  </section>

  <section class="card-front" aria-label="Postcard front">
    <div class="suit-art" role="img" aria-label="Illustration of a grey suit jacket with white shirt collar and red tie"></div>
    <div class="accent"></div>
    <div class="title-band"></div>
    <h1 class="title">All<br>Things<br>Employees</h1>
    <div class="brand">
      <span class="brand-dot"></span>
      <span class="brand-name">Staffwell Partners</span>
    </div>
  </section>

</body>
</html>
```